Employee Benefits and Insurance Consulting

We are an existing company with over 30 years experience but are changing our name. We would like a simple design with grey tones.

Industry/Entity Type

Insurance

Contact Information for Business Card

Marlow Benefits Consulting
Gerald P Odell CEO
5172 Brackenfield Road
Ashford, TN 37841
gerald@marlowbx.com
865-412-3396 - O
865-247-5081 - C

```html
<!DOCTYPE html>
<html lang="en">
<head>
<meta charset="utf-8">
<title>Marlow Benefits Consulting – Business Card</title>
<link href="https://fonts.googleapis.com/css2?family=Nunito+Sans:wght@400;700&display=swap" rel="stylesheet">
<style>
  :root {
    --page-bg: #e6e6e6;
    --card-bg: #ffffff;
    --navy: #1d3f78;
    --grey-text: #6a6a6a;
  }
  html, body {
    margin: 0;
    padding: 0;
    width: 1200px;
    height: 1000px;
    overflow: hidden;
    background: var(--page-bg);
    font-family: "Nunito Sans", Arial, sans-serif;
  }
  .business-card {
    position: absolute;
    left: 100px;
    top: 201px;
    width: 1000px;
    height: 598px;
    background: var(--card-bg);
    box-shadow: 0 4px 14px rgba(0, 0, 0, 0.18);
  }
  .brand {
    position: absolute;
    left: 70px;
    top: 158px;
    width: 410px;
    text-align: center;
  }
  .brand-square {
    display: block;
    width: 110px;
    height: 110px;
    margin: 20px auto 42px;
    background: var(--navy);
  }
  .brand-name {
    margin: 0;
    color: var(--navy);
    font-weight: 400;
    font-size: 40px;
    line-height: 1.15;
    letter-spacing: 1px;
    text-transform: uppercase;
  }
  .contact {
    position: absolute;
    left: 603px;
    top: 150px;
    color: var(--grey-text);
  }
  .person-name {
    margin: 0;
    color: var(--navy);
    font-weight: 700;
    font-size: 31px;
    line-height: 38px;
  }
  .person-title {
    margin: 0 0 34px;
    font-size: 24px;
    line-height: 30px;
  }
  .address {
    margin: 0 0 20px;
    font-style: normal;
    font-size: 26px;
    line-height: 36px;
  }
  .contact-list {
    list-style: none;
    margin: 0;
    padding: 0;
    font-size: 26px;
    line-height: 38px;
  }
  .contact-list li {
    display: flex;
    align-items: center;
  }
  .contact-icon {
    width: 22px;
    height: 22px;
    margin-right: 14px;
    fill: var(--navy);
  }
</style>
</head>
<body>
  <section class="business-card">
    <div class="brand">
      <span class="brand-square"></span>
      <p class="brand-name">Marlow Benefits Consulting</p>
    </div>

    <div class="contact">
      <h1 class="person-name">Gerald P Odell</h1>
      <p class="person-title">CEO</p>
      <address class="address">5172 Brackenfield Road<br>Ashford, TN 37841</address>
      <ul class="contact-list">
        <li>
          <svg class="contact-icon" viewBox="0 0 24 24" aria-hidden="true"><rect x="6" y="2" width="12" height="20" rx="2"/><rect x="8.5" y="5" width="7" height="6" fill="#fff"/><rect x="8.5" y="13" width="7" height="6" fill="#fff" opacity=".5"/></svg>
          865-412-3396
        </li>
        <li>
          <svg class="contact-icon" viewBox="0 0 24 24" aria-hidden="true"><path d="M2 9c0-3 4-5 10-5s10 2 10 5v2h-5V8.5c-1.5-.6-3.2-.9-5-.9s-3.5.3-5 .9V11H2z"/><path d="M6 12h12l2 8H4z"/><circle cx="12" cy="16" r="2" fill="#fff"/></svg>
          865-247-5081
        </li>
        <li>
          <svg class="contact-icon" viewBox="0 0 24 24" aria-hidden="true"><rect x="2" y="5" width="20" height="14" rx="1"/><path d="M3 6l9 7 9-7" fill="none" stroke="#fff" stroke-width="1.8"/></svg>
          gerald@marlowbx.com
        </li>
      </ul>
    </div>
  </section>
</body>
</html>
```